House Builder and Property Development Card Design and Logo

I need a business card design for a building and property development company.
Colour scheme of Dark Grey and Green, I would like it bold, sharp and professional.
No logo yet done, I'm open to options but please stay away from the usual- house, roof, hammers etc.
Thanks Lou
Updates

Please be aware that on the business card information section the VKRT # 5382917 is a licence number and my phone number 0461739258. The numbers are close together and could be mistaken as one whole number 

Thank you

                                   

Industry/Entity Type

Building

Contact Information for Business Card

HARLOW BUILD & DEVELOPMENT.
Residential Building & Property Development
Louis Harlow - Director
VKRT # 5382917
0461739258
lou@harlowbuild.com.au

Requirements
Must have
• Bold Business name
Dark grey and green colours
Should not have
• roof outline or hammer logo

```html
<!DOCTYPE html>
<html lang="en">
<head>
<meta charset="utf-8">
<title>Harlow Build &amp; Development – Business Card</title>
<link rel="stylesheet" href="https://fonts.googleapis.com/css2?family=Questrial&family=Libre+Caslon+Text:wght@700&family=Cinzel:wght@700&display=swap">
<style>
  :root {
    --card-black: #000000;
    --brand-green: #1a9250;
    --band-green: #056a3a;
    --tagline-grey: #8e8e8e;
    --licence-white: #f2f2f2;
  }
  html, body {
    margin: 0;
    padding: 0;
    overflow: hidden;
    background: var(--card-black);
  }
  .card {
    position: relative;
    width: 1200px;
    height: 695px;
    background: var(--card-black);
    overflow: hidden;
  }
  .brand {
    position: absolute;
    top: 208px;
    left: 0;
    width: 100%;
    text-align: center;
  }
  .brand-name {
    margin: 0;
    font-family: "Questrial", "Century Gothic", sans-serif;
    font-weight: 700;
    font-size: 47px;
    letter-spacing: 1px;
    color: var(--brand-green);
    line-height: 1;
    -webkit-text-stroke: 0.8px var(--brand-green);
  }
  .tagline {
    margin: 14px 0 0;
    font-family: "Libre Caslon Text", Georgia, serif;
    font-weight: 700;
    font-size: 33px;
    color: var(--tagline-grey);
    line-height: 1;
  }
  .licence-band {
    position: absolute;
    left: 0;
    bottom: 0;
    width: 100%;
    height: 79px;
    background: var(--band-green);
    display: flex;
    align-items: center;
    justify-content: center;
  }
  .licence-text {
    margin: 0;
    font-family: "Cinzel", "Copperplate", serif;
    font-weight: 700;
    font-size: 30px;
    letter-spacing: 1.5px;
    color: var(--licence-white);
    white-space: pre;
  }
</style>
</head>
<body>
  <main class="card">
    <header class="brand">
      <h1 class="brand-name">HARLOW BUILD &amp; DEVELOPMENT</h1>
      <p class="tagline">Residential Building &amp; Property Development</p>
    </header>
    <footer class="licence-band">
      <p class="licence-text">LICENCE NUMBER   /   VKRT # 5382917</p>
    </footer>
  </main>
</body>
</html>
```